Bramblecourt Homes Stationary
Fast Settlements
Professional
Dorian Pelletier
Managing Member
4817 Larkspur Ave Suite 210
Washington, DC
dgpelletier@bramblecourthomes.net
www.bramblecourthomes.net
Business License # 782645113058
Cash Buyer, Fast Closing.
Residential and Commercial
We are a Nation Wide Buyer.
will upload ai file shortly
vector logo file

```html
<!DOCTYPE html>
<html lang="en">
<head>
<meta charset="utf-8">
<title>Bramblecourt Homes Stationary</title>
<link rel="stylesheet" href="https://fonts.googleapis.com/css2?family=Michroma&display=swap">
<style>
  :root {
    --green: #2f9a3f;
    --green-dark: #1f7b2f;
    --ink: #3a3a3a;
    --muted: #6b6b6b;
    --paper: #ffffff;
    --backdrop: #ececea;
  }
  * { box-sizing: border-box; margin: 0; padding: 0; }
  html, body { width: 1200px; height: 629px; overflow: hidden; }
  body {
    background: var(--backdrop);
    font-family: "Michroma", sans-serif;
    color: var(--ink);
    position: relative;
  }
  .card {
    position: absolute;
    top: 162px;
    width: 525px;
    height: 300px;
    background: var(--paper);
    box-shadow: 0 6px 18px rgba(0,0,0,0.14);
    overflow: hidden;
  }
  .card--front { left: 50px; }
  .card--back { left: 625px; }

  .brand {
    display: flex;
    align-items: center;
    gap: 10px;
    color: var(--green);
    text-transform: uppercase;
    letter-spacing: 1px;
  }
  .brand__square {
    width: 22px; height: 22px;
    background: var(--green);
    flex: none;
  }
  .card--front .brand {
    position: absolute;
    top: 112px; left: 0; right: 0;
    justify-content: center;
    font-size: 22px;
  }
  .front__rule {
    position: absolute;
    top: 160px; left: 130px; right: 130px;
    height: 1px;
    background: var(--green);
  }
  .front__web {
    position: absolute;
    top: 172px; left: 0; right: 0;
    text-align: center;
    font-size: 10px;
    letter-spacing: 2px;
    color: var(--green);
    text-transform: uppercase;
  }

  .card--back .brand {
    position: absolute;
    top: 68px; left: 40px;
    font-size: 15px;
  }
  .card--back .brand__square { width: 18px; height: 18px; }
  .person {
    position: absolute;
    top: 128px; left: 40px;
    font-size: 8px;
    line-height: 1.6;
    text-transform: uppercase;
    letter-spacing: 0.5px;
  }
  .person__name { color: var(--green-dark); }
  .person__title { color: var(--muted); }
  .address {
    position: absolute;
    top: 200px; left: 40px;
    font-size: 7.5px;
    line-height: 1.7;
    color: var(--muted);
    text-transform: uppercase;
  }
  .contacts {
    position: absolute;
    top: 96px; left: 300px;
    list-style: none;
    font-size: 7.5px;
    color: var(--muted);
  }
  .contacts li {
    display: flex;
    align-items: center;
    gap: 8px;
    height: 17px;
  }
  .contacts svg { width: 11px; height: 11px; flex: none; }
  .band {
    position: absolute;
    left: 0; right: 0; bottom: 0;
    height: 44px;
    background: var(--green);
    color: #fff;
    font-size: 9px;
    letter-spacing: 2px;
    text-transform: uppercase;
    display: flex;
    align-items: center;
    justify-content: flex-end;
    padding-right: 30px;
  }
</style>
</head>
<body>
  <section class="card card--front">
    <div class="brand"><span class="brand__square"></span>Bramblecourt Homes</div>
    <div class="front__rule"></div>
    <p class="front__web">www.bramblecourthomes.net</p>
  </section>

  <section class="card card--back">
    <div class="brand"><span class="brand__square"></span>Bramblecourt Homes</div>
    <div class="person">
      <p class="person__name">Dorian Pelletier</p>
      <p class="person__title">Managing Member</p>
    </div>
    <div class="address">
      <p>4817 Larkspur Ave Suite 210</p>
      <p>Washington, DC 20006</p>
    </div>
    <ul class="contacts">
      <li><svg viewBox="0 0 12 12"><circle cx="6" cy="6" r="6" fill="var(--green)"/><path d="M4 3.2l1 .1.5 1.4-.7.6a4 4 0 0 0 1.9 1.9l.6-.7 1.4.5.1 1a1 1 0 0 1-1 .8A5 5 0 0 1 3.2 4.2 1 1 0 0 1 4 3.2z" fill="#fff"/></svg>1-800-555-0142</li>
      <li><svg viewBox="0 0 12 12"><circle cx="6" cy="6" r="6" fill="var(--green)"/><path d="M4 3.2l1 .1.5 1.4-.7.6a4 4 0 0 0 1.9 1.9l.6-.7 1.4.5.1 1a1 1 0 0 1-1 .8A5 5 0 0 1 3.2 4.2 1 1 0 0 1 4 3.2z" fill="#fff"/></svg>202-555-0187</li>
      <li><svg viewBox="0 0 12 12"><circle cx="6" cy="6" r="6" fill="var(--green)"/><rect x="3.5" y="3.2" width="5" height="5.6" rx=".6" fill="#fff"/></svg>410-555-0126</li>
      <li><svg viewBox="0 0 12 12"><circle cx="6" cy="6" r="6" fill="var(--green)"/><rect x="3" y="4" width="6" height="4" fill="#fff"/><path d="M3 4l3 2.2L9 4" stroke="var(--green)" stroke-width=".7" fill="none"/></svg>dgpelletier@bramblecourthomes.net</li>
      <li><svg viewBox="0 0 12 12"><circle cx="6" cy="6" r="6" fill="var(--green)"/><circle cx="6" cy="6" r="3" stroke="#fff" stroke-width=".8" fill="none"/><path d="M3 6h6M6 3v6" stroke="#fff" stroke-width=".6"/></svg>www.bramblecourthomes.net</li>
    </ul>
    <div class="band">www.bramblecourthomes.net</div>
  </section>
</body>
</html>
```